Real estate company needs a card that makes you say WOW!

We need an awesome business card for our real estate company, Stonebrook Realty Partners of Chicago, that will stand out from the crowd. We specialize in buying and selling real estate, property management, and real estate investments (Flips & Rentals). On the business card, I need the following:

- Our logo
- Services
- My name & contact info (Derek Ollanby, 630-517-2946, Derek@StonebrookRPC.com)
- My title (Director of Acquisitions)
- StonebrookRPC.com

I attached an EPS file of our logo. Let me know if you have any questions. Thank you in advance!

```html
<!DOCTYPE html>
<html lang="en">
<head>
<meta charset="utf-8">
<title>Stonebrook Realty Partners of Chicago – Business Card</title>
<link href="https://fonts.googleapis.com/css2?family=Crimson+Text:wght@400;600&family=Questrial&display=swap" rel="stylesheet">
<style>
  :root {
    --stage: #3a3a3a;
    --card-white: #ffffff;
    --brand-blue: #1a5d9c;
    --text-grey: #3b3b3b;
    --skyline-grey: #d9d9d9;
    --back-top: #29a6e2;
    --back-bottom: #155fa3;
    --icon-blue: #1f7fc8;
  }
  * { margin: 0; padding: 0; box-sizing: border-box; }
  html, body { width: 1000px; height: 1200px; overflow: hidden; }
  body { background: var(--stage); position: relative; }

  .card {
    position: absolute;
    width: 723px;
    height: 422px;
    overflow: hidden;
    box-shadow: 0 6px 18px rgba(0,0,0,0.45);
  }

  /* Front */
  .card-front {
    left: 117px; top: 100px;
    background: linear-gradient(to bottom, var(--card-white) 45%, #eeeeee 100%);
  }
  .holder-name {
    position: absolute; right: 35px; top: 50px;
    font-family: "Questrial", sans-serif;
    font-weight: 400;
    font-size: 31px; color: var(--brand-blue);
  }
  .holder-title {
    position: absolute; right: 35px; top: 88px;
    font-family: "Crimson Text", serif;
    font-size: 22px; color: var(--text-grey);
  }
  .company-name {
    position: absolute; left: 30px; top: 170px;
    width: 340px;
    font-family: "Crimson Text", serif;
    font-weight: 400;
    font-size: 30px; line-height: 1.15;
    color: var(--brand-blue);
    text-align: center;
    white-space: nowrap;
  }
  .company-name .mark {
    display: block;
    width: 34px; height: 34px;
    margin: 0 auto 14px;
    border-radius: 50%;
    background: var(--brand-blue);
  }
  .company-name .line { display: block; }
  .skyline-faint {
    position: absolute; left: 0; right: 0; bottom: 0; height: 150px;
    background: linear-gradient(to bottom, rgba(217,217,217,0) 0%, var(--skyline-grey) 100%);
  }
  .contact {
    position: absolute; right: 35px;
    display: flex; align-items: center; gap: 8px;
    font-family: "Crimson Text", serif;
    font-size: 21px; color: var(--text-grey);
  }
  .contact-phone { top: 300px; }
  .contact-email { top: 334px; }
  .contact-web { top: 368px; }
  .contact svg { width: 28px; height: 28px; }

  /* Back */
  .card-back {
    left: 128px; top: 656px;
    background: linear-gradient(to bottom, var(--back-top) 0%, var(--back-bottom) 100%);
    text-align: center; color: #fff;
  }
  .services-heading {
    position: absolute; left: 0; right: 0; top: 90px;
    font-family: "Questrial", sans-serif;
    font-weight: 400;
    font-size: 33px; letter-spacing: 0.5px;
  }
  .services-list {
    position: absolute; left: 0; right: 0; top: 140px;
    list-style: none;
    font-family: "Crimson Text", serif;
    font-weight: 600; font-size: 22px; line-height: 33px;
  }
  .skyline-white {
    position: absolute; left: 0; right: 0; bottom: 0; height: 150px;
    background: linear-gradient(to bottom, rgba(255,255,255,0) 0%, rgba(255,255,255,0.85) 45%, #ffffff 100%);
  }
</style>
</head>
<body>

<section class="card card-front">
  <div class="skyline-faint" role="img" aria-label="Faint grey Chicago skyline silhouette"></div>

  <h1 class="holder-name">Derek Ollanby</h1>
  <p class="holder-title">Director of Acquisitions</p>

  <p class="company-name"><span class="mark"></span><span class="line">Stonebrook Realty Partners</span><span class="line">of Chicago</span></p>

  <p class="contact contact-phone">630-517-2946
    <svg viewBox="0 0 28 28" aria-hidden="true">
      <circle cx="14" cy="14" r="14" fill="var(--icon-blue)"/>
      <path d="M10 7c1 0 2 2.5 2 3.2 0 .8-1.2 1.2-1.2 2 0 1.5 2.7 4.2 4.2 4.2.8 0 1.2-1.2 2-1.2.7 0 3.2 1 3.2 2 0 1.5-1.7 2.8-3 2.8-4.2 0-9.2-5-9.2-9.2C8 8.7 9 7 10 7z" fill="#fff"/>
    </svg>
  </p>
  <p class="contact contact-email">Derek@StonebrookRPC.com
    <svg viewBox="0 0 28 28" aria-hidden="true">
      <circle cx="14" cy="14" r="14" fill="var(--icon-blue)"/>
      <rect x="7" y="9" width="14" height="10" rx="1" fill="#fff"/>
      <path d="M7.5 9.5 14 15l6.5-5.5" fill="none" stroke="var(--icon-blue)" stroke-width="1.3"/>
    </svg>
  </p>
  <p class="contact contact-web">StonebrookRPC.com
    <svg viewBox="0 0 28 28" aria-hidden="true">
      <circle cx="14" cy="14" r="14" fill="var(--icon-blue)"/>
      <circle cx="14" cy="14" r="7" fill="none" stroke="#fff" stroke-width="1.4"/>
      <ellipse cx="14" cy="14" rx="3" ry="7" fill="none" stroke="#fff" stroke-width="1.2"/>
      <path d="M7 14h14" stroke="#fff" stroke-width="1.2"/>
    </svg>
  </p>
</section>

<section class="card card-back">
  <h2 class="services-heading">WE SPECIALIZE IN</h2>
  <ul class="services-list">
    <li>Buying and Selling Real Estate,</li>
    <li>Property Management,</li>
    <li>Real Estate Investments (Flips &amp; Rentals)</li>
  </ul>
  <div class="skyline-white" role="img" aria-label="White Chicago skyline silhouette"></div>
</section>

</body>
</html>
```